Oil and Gas Exploration and Production company needs a business card design

We need a business card design using our logo and colors in the logo. We want a mainstream design.

```html
<!DOCTYPE html>
<html lang="en">
<head>
<meta charset="utf-8">
<title>Tarma Oil &amp; Gas – Business Card</title>
<link rel="stylesheet" href="https://fonts.googleapis.com/css2?family=Fira+Sans:wght@300;400;700&family=Fira+Mono&display=swap">
<style>
  :root {
    --canvas: #d9d9d9;
    --paper: #ebe9e4;
    --paper-shade: #dcd9d2;
    --gold: #b07a18;
    --gold-deep: #8d5f0e;
    --ink: #141210;
    --band-line: #e9dcc0;
    --brown-light: #a0701c;
    --brown-mid: #6e4a12;
    --brown-dark: #2e1f0a;
    --mark-ink: rgba(30, 20, 8, 0.72);
  }
  * { box-sizing: border-box; margin: 0; padding: 0; }
  html, body { width: 1200px; height: 1200px; overflow: hidden; }
  body {
    background: linear-gradient(180deg, #f4f4f4 0%, var(--canvas) 100%);
    font-family: "Fira Sans", sans-serif;
    position: relative;
  }
  .card {
    position: absolute;
    left: 150px;
    width: 900px;
    height: 514px;
    overflow: hidden;
    box-shadow: 0 14px 30px rgba(0,0,0,0.22);
  }
  .card-front { top: 50px; background: radial-gradient(ellipse at 30% 20%, #f3f2ef 0%, var(--paper) 55%, var(--paper-shade) 100%); }
  .card-back  { top: 620px; background: radial-gradient(ellipse at 40% 45%, var(--brown-light) 0%, var(--brown-mid) 55%, var(--brown-dark) 100%); }

  .band { position: absolute; inset: 0; width: 100%; height: 100%; }

  .brand {
    position: absolute;
    left: 80px;
    top: 100px;
    width: 420px;
    display: flex;
    align-items: flex-start;
    gap: 16px;
    font-weight: 700;
    font-size: 62px;
    line-height: 1.02;
    color: var(--ink);
    letter-spacing: -0.5px;
  }
  .brand-dot { width: 38px; height: 38px; margin-top: 16px; border-radius: 50%; background: var(--ink); flex: none; }
  .brand-name { display: block; }

  .contact {
    position: absolute;
    left: 540px;
    top: 110px;
    width: 330px;
    color: var(--ink);
    font-size: 17px;
    line-height: 1.35;
  }
  .contact-name { font-weight: 300; font-size: 34px; line-height: 1.15; color: var(--gold); text-transform: uppercase; letter-spacing: 0.5px; }
  .contact-role { font-size: 17px; margin-bottom: 18px; }
  .contact-address { margin-bottom: 18px; }
  .contact-lines { font-family: "Fira Mono", monospace; font-size: 17px; }
  .contact-lines dt { float: left; width: 80px; font-family: "Fira Sans", sans-serif; }
  .contact-lines dd { margin-left: 80px; }
  .contact-email { font-family: "Fira Mono", monospace; }

  .website {
    position: absolute;
    left: 150px;
    bottom: 38px;
    font-family: "Fira Mono", monospace;
    font-size: 20px;
    letter-spacing: 3px;
    color: var(--ink);
  }

  .back-brand {
    position: absolute;
    inset: 0;
    display: flex;
    align-items: center;
    justify-content: center;
    font-weight: 700;
    font-size: 96px;
    color: var(--mark-ink);
    letter-spacing: -1px;
  }
</style>
</head>
<body>

  <section class="card card-front" aria-label="Business card front">
    <svg class="band" viewBox="0 0 900 514" preserveAspectRatio="none" aria-hidden="true">
      <path d="M0,280 C150,285 250,320 360,370 S540,440 640,440 S810,460 900,450 L900,514 L0,514 Z" fill="var(--gold)"/>
      <path d="M0,280 C150,285 250,320 360,370 S540,440 640,440 S810,460 900,450" fill="none" stroke="var(--gold-deep)" stroke-width="4"/>
      <line x1="0" y1="300" x2="900" y2="472" stroke="var(--band-line)" stroke-width="1.5"/>
    </svg>

    <div class="brand">
      <span class="brand-dot"></span>
      <span class="brand-name">Tarma<br>Oil &amp; Gas</span>
    </div>

    <div class="contact">
      <p class="contact-name">Alex Moreno</p>
      <p class="contact-role">Director</p>
      <p class="contact-address">Dummy city<br>Dummy Country Land</p>
      <p class="contact-email">alex@tarmaoilgas.com</p>
      <dl class="contact-lines">
        <dt>Phone</dt><dd>1-555-014020</dd>
        <dt>Fax</dt><dd>1-555-014021</dd>
      </dl>
    </div>

    <p class="website">www.tarmaoilgas.com</p>
  </section>

  <section class="card card-back" aria-label="Business card back">
    <div class="back-brand">Tarma Oil &amp; Gas</div>
  </section>

</body>
</html>
```